Business Card for Professional Photographer

I'm looking for an eye catching modern clean design that compliments my logo/ website fonts & colours.
I specialise in architecture, corporate & commercial photography so I'm marketing to professional clients rather than portrait / wedding clients.

I would prefer to not have a solid black design.

My logo brand guide is as follows :

Main front font. : Reislust
Main font colour : #fff
Slogan front font : Ubuntu Bold
Monogram front font : Venti Medium
Container colour : #fff

I need print ready files in pdf .png & .eps formats.

Included in the files below are some screen grabs as reference to font & colours etc.

```html
<!DOCTYPE html>
<html lang="en">
<head>
<meta charset="utf-8">
<title>Northlight Frame – Business Card</title>
<link rel="stylesheet" href="https://fonts.googleapis.com/css2?family=Josefin+Sans:wght@300&family=Montserrat:wght@400;600&family=Ubuntu:wght@700&display=swap">
<style>
  :root{
    --backdrop:#5f5f5f;
    --card-white:#ffffff;
    --gold-dark:#b8803d;
    --gold-light:#e4b97c;
    --ink:#111111;
    --ink-soft:#2a2a2a;
    --wordmark-grey:#3a3a3a;
  }
  *{margin:0;padding:0;box-sizing:border-box}
  html,body{width:1200px;height:960px;overflow:hidden}
  body{background:var(--backdrop);position:relative;font-family:"Montserrat",sans-serif}

  .card{position:absolute;width:560px;height:320px;border-radius:24px;overflow:hidden;box-shadow:0 14px 30px rgba(0,0,0,.35)}
  .card--front{left:60px;top:110px;background:var(--card-white)}
  .card--back{left:580px;top:520px;background:linear-gradient(120deg,var(--gold-dark) 0%,#cc9a5a 55%,var(--gold-light) 100%)}

  .brand{display:flex;align-items:center;gap:18px}
  .brand__mark{width:46px;height:46px;border-radius:50%;background:linear-gradient(135deg,var(--gold-dark),var(--gold-light));flex:none}
  .brand__name{font-family:"Josefin Sans",sans-serif;font-weight:300;letter-spacing:.22em;text-transform:uppercase;line-height:1}
  .brand__tagline{font-family:"Ubuntu",sans-serif;font-weight:700;letter-spacing:.12em;margin-top:4px}

  .card--front .brand{position:absolute;left:96px;top:132px}
  .card--front .brand__name{font-size:32px;color:var(--wordmark-grey)}
  .card--front .brand__tagline{font-size:10px;color:var(--wordmark-grey)}

  .back-decoration{position:absolute;right:70px;top:50px;width:70px;height:70px;border-radius:12px;border:3px solid rgba(120,80,30,.35)}

  .back-content{position:absolute;left:52px;top:56px;color:var(--ink)}
  .card--back .brand__name{font-size:22px;color:var(--ink)}
  .card--back .brand__tagline{font-size:7px;color:var(--ink)}

  .person{margin-top:26px}
  .person__name{font-weight:600;font-size:16px;letter-spacing:.02em;text-transform:uppercase}
  .person__role{font-size:13px;color:var(--ink-soft);margin-top:2px}

  .address{margin-top:14px;font-size:13px;line-height:1.25}

  .contacts{list-style:none;margin-top:14px;font-size:12.5px;line-height:1.3}
  .contacts li{display:flex;align-items:center;gap:8px}
  .contacts svg{width:11px;height:11px;flex:none;fill:var(--ink)}
</style>
</head>
<body>

<section class="card card--front" aria-label="Card front">
  <div class="brand">
    <span class="brand__mark"></span>
    <div>
      <div class="brand__name">Northlight Frame</div>
      <div class="brand__tagline">Architecture Corporate Commercial</div>
    </div>
  </div>
</section>

<section class="card card--back" aria-label="Card back">
  <span class="back-decoration"></span>
  <div class="back-content">
    <div class="brand__name">Northlight Frame</div>
    <div class="brand__tagline">Architecture Corporate Commercial</div>

    <div class="person">
      <div class="person__name">Daniel Reyes</div>
      <div class="person__role">President</div>
    </div>

    <address class="address" style="font-style:normal">
      412 Harbor View Road<br>Juneau, Alaska 99801
    </address>

    <ul class="contacts">
      <li><svg viewBox="0 0 24 24"><path d="M6.6 10.8a15 15 0 0 0 6.6 6.6l2.2-2.2a1 1 0 0 1 1-.25 11.4 11.4 0 0 0 3.6.6 1 1 0 0 1 1 1V20a1 1 0 0 1-1 1A17 17 0 0 1 3 4a1 1 0 0 1 1-1h3.5a1 1 0 0 1 1 1c0 1.25.2 2.45.6 3.6a1 1 0 0 1-.25 1z"/></svg>555-201-4830</li>
      <li><svg viewBox="0 0 24 24"><path d="M7 1h10a2 2 0 0 1 2 2v18a2 2 0 0 1-2 2H7a2 2 0 0 1-2-2V3a2 2 0 0 1 2-2zm0 3v14h10V4z"/></svg>555-318-2746</li>
      <li><svg viewBox="0 0 24 24"><path d="M6 2h10v5H6zM3 8h18v10h-3v4H6v-4H3zm5 7v5h8v-5z"/></svg>555-402-6159</li>
      <li><svg viewBox="0 0 24 24"><path d="M2 5h20v14H2zm2 2v.5l8 5 8-5V7z"/></svg>info@northlightframe.com</li>
      <li><svg viewBox="0 0 24 24"><circle cx="12" cy="12" r="10"/></svg>www.northlightframe.com</li>
    </ul>
  </div>
</section>

</body>
</html>
```